Design for Screen Wash Tablet Tube New product

I have a tube which holds screenwash tablets which I need Label created for... Label is 90mm x 90mm. It must include
> logo attached,
>the catchphrase ( drop,dissolve,wash. )
>6 Tablets inside
>1 Tablet makes 5 litres screen wash
>Room for ingredients section( around 20 words)
> Caution - Harmful if swallowed. May cause skin Irritation or eye damage. Do not eat,drink or smoke when using this product. If medical advice is needed have product packaging to hand. Store in a clean dry place.
>Keep out of reach of Children
>Barcode area
>Directions of use
Place tablet in Screenwash bottle
Simply add water
>Product will take approximately 5-10 minutes to fully dissolve.
>3 harmful logo attached
>Cherry Fragrance
Target Market(s)
retail sector - grocery fmcg and car/auto stores
Industry/Entity Type
car care

```html
<!DOCTYPE html>
<html lang="en">
<head>
<meta charset="utf-8">
<title>ShineDrift Screenwash Tablets Label</title>
<link href="https://fonts.googleapis.com/css2?family=Anton&family=Oswald:wght@500;600&family=Poppins:ital,wght@0,400;0,700;1,400&family=Arimo&display=swap" rel="stylesheet">
<style>
  :root {
    --teal-dark: #0b6763;
    --teal-mid: #12847f;
    --teal-light: #1ea29c;
    --red: #e01b2b;
    --red-deep: #a8111c;
    --magenta: #b0246a;
    --yellow: #fcd21d;
    --white: #ffffff;
    --ink: #1b1b1b;
  }
  * { margin: 0; padding: 0; box-sizing: border-box; }
  html, body { width: 1200px; height: 900px; overflow: hidden; background: var(--white); }
  .canvas { position: relative; width: 1200px; height: 900px; }
  .label {
    position: absolute; left: 243px; top: 93px; width: 714px; height: 714px;
    box-shadow: 0 6px 22px rgba(11, 103, 99, 0.55);
    overflow: hidden;
  }
  .label-art { position: absolute; inset: 0; width: 714px; height: 714px; }
  .brand-name {
    position: absolute; left: 0; width: 340px; top: 30px; text-align: center;
    font-family: 'Poppins', sans-serif; font-weight: 700; font-size: 25px; color: var(--red);
  }
  .product-title { position: absolute; left: 0; width: 340px; top: 98px; text-align: center; }
  .title-line {
    display: inline-block; font-family: 'Anton', sans-serif; color: var(--white);
    background: linear-gradient(180deg, var(--red), var(--red-deep));
    border-radius: 6px; line-height: 1; letter-spacing: -1px;
    box-shadow: 0 3px 6px rgba(0,0,0,0.25);
  }
  .title-line--small { font-size: 44px; padding: 4px 10px 2px; }
  .title-line--large { font-size: 66px; padding: 2px 10px 4px; margin-top: -6px; }
  .fragrance {
    position: absolute; left: 0; width: 340px; top: 228px; text-align: center;
    font-family: 'Poppins', sans-serif; font-style: italic; font-size: 19px; color: var(--magenta);
  }
  .catchphrase {
    position: absolute; left: 0; width: 330px; top: 515px; text-align: center;
    font-family: 'Oswald', sans-serif; font-weight: 600; font-size: 45px; line-height: 1;
    color: var(--yellow); letter-spacing: -1.5px;
  }
  .count {
    position: absolute; left: 0; width: 320px; top: 573px; text-align: center;
    font-family: 'Oswald', sans-serif; font-weight: 500; font-size: 28px; line-height: 1;
    color: var(--white); letter-spacing: -0.5px;
  }
  .yield {
    position: absolute; left: 0; width: 320px; top: 614px; text-align: center;
    font-family: 'Arimo', sans-serif; font-size: 18.5px; line-height: 17px; color: var(--white);
  }
  .info {
    position: absolute; left: 373px; width: 315px;
    font-family: 'Poppins', sans-serif; font-size: 16px; line-height: 20.2px; color: var(--white);
  }
  .info--ingredients { top: 36px; }
  .info--directions { top: 164px; }
  .info--caution { top: 293px; }
  .barcode-area {
    position: absolute; left: 403px; top: 529px; width: 236px; height: 165px;
    background: var(--white); border: 1px solid var(--ink);
  }
</style>
</head>
<body>
<div class="canvas">
  <div class="label">
    <svg class="label-art" viewBox="0 0 1310 1310" xmlns="http://www.w3.org/2000/svg">
      <defs>
        <radialGradient id="tealGlow" cx="0.5" cy="0.45" r="0.65">
          <stop offset="0" stop-color="#1ea29c"/>
          <stop offset="1" stop-color="#0b6763"/>
        </radialGradient>
        <linearGradient id="carTone" x1="0" y1="0" x2="1" y2="1">
          <stop offset="0" stop-color="#1a8f95"/>
          <stop offset="0.45" stop-color="#0c3f44"/>
          <stop offset="1" stop-color="#050d10"/>
        </linearGradient>
        <linearGradient id="swoosh" x1="0" y1="1" x2="1" y2="0">
          <stop offset="0" stop-color="#a8111c"/>
          <stop offset="0.6" stop-color="#e01b2b"/>
          <stop offset="1" stop-color="#b5121e"/>
        </linearGradient>
        <clipPath id="heroClip">
          <path d="M0,0 H460 C620,120 690,330 673,480 C660,760 440,1068 90,1070 L0,1070 Z"/>
        </clipPath>
      </defs>

      <rect class="backdrop" width="1310" height="1310" fill="url(#tealGlow)"/>
      <path class="hero-panel" d="M0,0 H460 C620,120 690,330 673,480 C660,760 440,1068 90,1070 L0,1070 Z" fill="#ffffff"/>
      <g clip-path="url(#heroClip)">
        <path class="hero-photo" role="img" aria-label="Photo of a glossy dark sports car front, teal-lit"
              d="M0,540 C150,510 420,505 560,520 C640,540 700,600 700,640 V1100 H0 Z" fill="url(#carTone)"/>
      </g>

      <path class="bottom-sweep" d="M0,1310 C320,1260 560,1150 780,1050 C960,960 1150,880 1310,1000 V1310 Z" fill="#ffffff"/>
      <path class="sweep-line" d="M20,1310 C330,1255 560,1145 760,1045" fill="none" stroke="url(#swoosh)" stroke-width="16"/>
      <path class="sweep-line" d="M900,965 C1060,905 1220,900 1310,1000" fill="none" stroke="url(#swoosh)" stroke-width="18"/>

      <g class="hazard hazard--corrosive" transform="translate(765,883)">
        <rect x="-48" y="-48" width="96" height="96" transform="rotate(45)" fill="#ffffff" stroke="#e01b2b" stroke-width="11"/>
        <rect x="-34" y="-18" width="68" height="36" rx="4" fill="#9a9a9a" role="img" aria-label="Corrosive hazard pictogram"/>
      </g>
      <g class="hazard hazard--environment" transform="translate(955,883)">
        <rect x="-48" y="-48" width="96" height="96" transform="rotate(45)" fill="#ffffff" stroke="#e01b2b" stroke-width="11"/>
        <rect x="-30" y="-28" width="60" height="52" rx="4" fill="#9a9a9a" role="img" aria-label="Environmental hazard pictogram"/>
      </g>
      <g class="hazard hazard--irritant" transform="translate(1148,883)">
        <rect x="-48" y="-48" width="96" height="96" transform="rotate(45)" fill="#ffffff" stroke="#e01b2b" stroke-width="11"/>
        <path d="M-7,-38 H7 L4,14 H-4 Z" fill="#111111"/>
        <circle cx="0" cy="28" r="8" fill="#111111"/>
      </g>
    </svg>

    <div class="brand-name">ShineDrift</div>
    <div class="product-title">
      <span class="title-line title-line--small">SCREENWASH</span><br>
      <span class="title-line title-line--large">TABLETS</span>
    </div>
    <div class="fragrance">Cherry Fragrance</div>

    <div class="catchphrase">Drop,Dissolve,Wash</div>
    <div class="count">6 Tablets inside</div>
    <div class="yield">1 Tablet makes<br>5 litres screen wash</div>

    <p class="info info--ingredients">Ingredients: Lorem ipsum dolor sit amet, consectetuer adipiscing elit, sed diam nonummy nibh euismod tincidunt ut laoreet dolore magna aliquam erat volutpat. Ut wisi enim</p>
    <p class="info info--directions">Directions of use<br>Place tablet in Screenwash bottle<br>Simply add water<br>Product will take approximately 5-10 minutes to fully dissolve.</p>
    <p class="info info--caution">Caution - Harmful if swallowed. May cause skin Irritation or eye damage. Do not eat,drink or smoke when using this product. If medical advice is needed have product packaging to hand. Store in a clean dry place.</p>

    <div class="barcode-area"></div>
  </div>
</div>
</body>
</html>
```